Business Card Design Project

The business card is for an educational company that provides personalised tuition to students.

The company logo is in orange and blue (as provided) and should be included in the name card design

The philosophy of the company is to make learning a comfortable experience for student as such design of the namecard should look fresh and has a bit of the 'wow' factor. Some of the namecard design that appeals to me are as uploaded under Sample Design.

The particulars that need to be provided are:
(1): Company Name (Quillmark Education)
(1): Name
(2): Educational qualifications which will appear below name
(3): Mobile number
(4): Email address
(5): Website

Industry/Entity Type

Business

Requirements
Must have
• (1): Company Logo

(2): The card background should preferably be coloured both for the front side and back.

(3): The choice of font is important as part of the selection consideration. There is no preferred font that I have selected, designer is free to choose the font that will complement their design.

```html
<!DOCTYPE html>
<html lang="en">
<head>
<meta charset="utf-8">
<title>Quillmark Education — Business Card</title>
<link href="https://fonts.googleapis.com/css2?family=Quicksand:wght@400;500;600&display=swap" rel="stylesheet">
<style>
  :root {
    --page-bg: #e6e8ea;
    --card-bg: #5e5e60;
    --card-shade: #535355;
    --text-light: #f2f2f2;
    --text-soft: #dcdcdc;
    --accent-orange: #f07a1c;
    --pattern-tone: #505052;
  }
  * { margin: 0; padding: 0; box-sizing: border-box; }
  html, body {
    width: 1200px; height: 960px; overflow: hidden;
    background: var(--page-bg);
    font-family: "Quicksand", "Helvetica Neue", Arial, sans-serif;
  }
  .sheet {
    width: 1200px; height: 960px;
    display: flex; flex-direction: column; align-items: center; justify-content: center;
    gap: 60px;
  }
  .card {
    position: relative;
    width: 630px; height: 360px;
    background: var(--card-bg);
    border-radius: 4px;
    box-shadow: 0 6px 18px rgba(0,0,0,0.18);
    overflow: hidden;
  }
  .brand {
    position: absolute;
    display: flex; align-items: center; gap: 16px;
    color: var(--text-light);
    font-family: "Quicksand", "Helvetica Neue", Arial, sans-serif;
    font-weight: 600;
    line-height: 1.05;
  }
  .brand-square {
    flex: none;
    background: var(--accent-orange);
    border-radius: 8px;
  }
  .brand-name { font-size: 34px; }

  /* front */
  .card-front .brand { left: 34px; top: 40px; }
  .card-front .brand-square { width: 84px; height: 84px; }
  .pattern-front {
    position: absolute; left: 0; bottom: 0;
    width: 210px; height: 170px;
    background: radial-gradient(ellipse at 30% 70%, var(--pattern-tone), var(--card-bg) 72%);
  }
  .person { position: absolute; left: 360px; top: 160px; color: var(--text-light); }
  .person-name { font-size: 25px; font-weight: 400; letter-spacing: 0.3px; }
  .person-role { font-size: 17px; font-weight: 400; color: var(--text-soft); margin-top: 4px; }
  .contacts {
    position: absolute; left: 340px; top: 252px;
    list-style: none; color: var(--text-light); font-size: 15.5px;
  }
  .contacts li { display: flex; align-items: center; gap: 10px; height: 24px; }
  .contacts svg { width: 14px; height: 14px; flex: none; }

  /* back */
  .card-back .brand { right: 40px; bottom: 52px; }
  .card-back .brand-square { width: 96px; height: 64px; }
  .card-back .brand-name { font-size: 38px; }
  .pattern-back {
    position: absolute; left: 0; top: 0;
    width: 420px; height: 210px;
    background: radial-gradient(ellipse at 35% 30%, var(--pattern-tone), var(--card-bg) 70%);
  }
</style>
</head>
<body>
<main class="sheet">

  <section class="card card-front">
    <div class="brand">
      <span class="brand-square"></span>
      <span class="brand-name">Quillmark<br>Education</span>
    </div>
    <div class="pattern-front" role="img" aria-label="Faint pattern of flying birds"></div>
    <div class="person">
      <p class="person-name">Miranda Colville</p>
      <p class="person-role">Operation Manager</p>
    </div>
    <ul class="contacts">
      <li>
        <svg viewBox="0 0 14 14" aria-hidden="true"><rect x="4" y="1" width="6" height="12" rx="1" fill="none" stroke="#f07a1c" stroke-width="1.4"/><rect x="5.5" y="3" width="3" height="4" fill="#f07a1c"/></svg>
        (555) 01 234 56 78
      </li>
      <li>
        <svg viewBox="0 0 14 14" aria-hidden="true"><rect x="1" y="3" width="12" height="8" fill="none" stroke="#f07a1c" stroke-width="1.4"/><path d="M1 3 L7 8 L13 3" fill="none" stroke="#f07a1c" stroke-width="1.4"/></svg>
        name@quillmark-education.com
      </li>
      <li>
        <svg viewBox="0 0 14 14" aria-hidden="true"><circle cx="7" cy="7" r="5.8" fill="#f07a1c"/><path d="M4 5 Q6 4 7 6 T10 9" fill="none" stroke="#5e5e60" stroke-width="1.3"/></svg>
        www.quillmark-education.com
      </li>
    </ul>
  </section>

  <section class="card card-back">
    <div class="pattern-back" role="img" aria-label="Faint pattern of flying birds"></div>
    <div class="brand">
      <span class="brand-square"></span>
      <span class="brand-name">Quillmark<br>Education</span>
    </div>
  </section>

</main>
</body>
</html>
```